Flyer

I am a qualified accountant and I need a flyer to promote my business when networking

My services include
Management Accounts, Financial Accounts, Day to Day Bookkeeping services, business start up assistance
I will produce and submit Self Assessment Tax Returns, Annual Accounts, VAT tax returns, Payroll and PAYE

I attach my business card design so that there is some continuity if you think it appropiate.

Size A3 is preferred, please.

Sorry, I mean't Size A5 is preferred.

A5 please

Free initial consultations and advice.                                   

Business

```html
<!DOCTYPE html>
<html lang="en">
<head>
<meta charset="utf-8">
<title>Clara Penrose Accounting – Flyer</title>
<link href="https://fonts.googleapis.com/css2?family=Exo+2:wght@200;300;400;600;700&display=swap" rel="stylesheet">
<style>
  :root {
    --green: #8cc63f;
    --green-text: #7cbf3a;
    --green-light: #a3cf4a;
    --band: #bfd93a;
    --band-edge: #96c93d;
    --paper: #f7f7f7;
    --white: #ffffff;
    --logo-green: #3f7d1f;
  }
  * { margin: 0; padding: 0; box-sizing: border-box; }
  html, body { width: 933px; height: 1200px; overflow: hidden; background: var(--white); }
  body { font-family: "Exo 2", sans-serif; }

  .flyer { position: relative; width: 933px; height: 1200px; background: var(--white); overflow: hidden; }

  .content-column {
    position: absolute; left: 0; top: 0; width: 508px; height: 1010px;
    background: linear-gradient(180deg, var(--white), var(--paper));
  }
  .photo-panel {
    position: absolute; left: 508px; top: 0; width: 368px; height: 1010px;
    background: linear-gradient(160deg, #f4ede6 0%, #dfe7ef 30%, #9aa3ab 55%, #5a6066 75%, #c9d6e6 100%);
  }

  .headline { position: absolute; left: 44px; top: 30px; color: var(--green); line-height: 0.95; text-transform: uppercase; }
  .headline .light { display: block; font-weight: 200; font-size: 86px; letter-spacing: 1px; }
  .headline .bold { display: block; font-weight: 700; font-size: 84px; }

  .rule { position: absolute; left: 44px; width: 432px; height: 3px; background: var(--green); }
  .rule.top { top: 296px; }
  .rule.bottom { top: 863px; }

  .name { position: absolute; left: 44px; top: 326px; color: var(--green); }
  .name h1 { font-weight: 600; font-size: 62px; line-height: 1; letter-spacing: -0.5px; }
  .name .credentials { font-weight: 200; font-size: 40px; line-height: 1.1; }

  .services { position: absolute; left: 44px; color: var(--green-text); text-transform: uppercase; }
  .services .intro { font-weight: 300; font-size: 22px; color: var(--green-light); margin-bottom: 26px; }
  .services ul { list-style: none; font-weight: 400; font-size: 23px; line-height: 26.5px; }
  .services.primary { top: 468px; }
  .services.secondary { top: 653px; }

  .offer { position: absolute; left: 44px; top: 914px; color: var(--green-text); font-weight: 300; font-size: 31px; line-height: 35px; text-transform: uppercase; }
  .offer strong { font-weight: 700; }

  .contact-band {
    position: absolute; left: 0; top: 1010px; width: 933px; height: 190px;
    background: var(--band); border-top: 12px solid var(--band-edge);
  }
  .brand { position: absolute; left: 44px; top: 93px; color: var(--logo-green); font-weight: 400; font-size: 19px; letter-spacing: 0.5px; text-transform: uppercase; }

  .contact-icon { position: absolute; left: 360px; }
  .contact-icon.phone { top: 40px; }
  .contact-icon.email { top: 110px; }

  .phone-number { position: absolute; right: 58px; top: 28px; color: var(--white); font-weight: 300; font-size: 64px; letter-spacing: 1px; }
  .email-address { position: absolute; right: 58px; top: 102px; color: var(--white); font-weight: 400; font-size: 28px; line-height: 29px; text-align: right; }
</style>
</head>
<body>
<main class="flyer">
  <section class="content-column">
    <div class="headline">
      <span class="light">Keeping</span>
      <span class="bold">You</span>
      <span class="bold">Ahead...</span>
    </div>

    <div class="rule top"></div>

    <div class="name">
      <h1>CLARA PENROSE</h1>
      <p class="credentials">ACMA / CGMA</p>
    </div>

    <div class="services primary">
      <p class="intro">My services include -</p>
      <ul>
        <li>Management Accounts</li>
        <li>Financial Accounts</li>
        <li>Day to Day Bookeeping Services</li>
        <li>Business Start-Up Assistance</li>
      </ul>
    </div>

    <div class="services secondary">
      <p class="intro">I will produce &amp; submit -</p>
      <ul>
        <li>Self Assessment Tax Returns</li>
        <li>Annual Returns</li>
        <li>VAT Tax Returns</li>
        <li>Payroll</li>
        <li>PAYE</li>
      </ul>
    </div>

    <div class="rule bottom"></div>

    <p class="offer"><strong>Free</strong> initial<br>consultations &amp; advice</p>
  </section>

  <div class="photo-panel" role="img" aria-label="Close-up photo of a finger pressing keys on a calculator resting on printed financial spreadsheets"></div>

  <footer class="contact-band">
    <p class="brand">Clara Penrose Accounting</p>

    <svg class="contact-icon phone" width="62" height="62" viewBox="0 0 62 62" aria-hidden="true">
      <circle cx="31" cy="31" r="27" fill="none" stroke="#fff" stroke-width="4"/>
      <path d="M22 17c2-1 4-1 5 1l3 6c1 2 0 3-1 4l-2 2c2 4 5 7 9 9l2-2c1-1 2-2 4-1l6 3c2 1 2 3 1 5l-2 3c-2 2-5 2-8 1-10-4-17-11-21-21-1-3-1-6 1-8z" fill="#fff"/>
    </svg>
    <svg class="contact-icon email" width="62" height="62" viewBox="0 0 62 62" aria-hidden="true">
      <text x="31" y="48" text-anchor="middle" font-family="Exo 2, sans-serif" font-size="60" font-weight="400" fill="#fff">@</text>
    </svg>

    <p class="phone-number">07700 900482</p>
    <p class="email-address">clara@<br>clarapenroseaccounting.com</p>
  </footer>
</main>
</body>
</html>
```